Road Construction Company needs business cards

We would like a new business card designed for our business.

We're a road construction company based in Qld, Australia.

Can the business card please have the following information on it.

Name: Brent Malvoy
Position: General Manager
Phone: 0471 592 304
Email: Brent.malvoy@quendix.com.au
Address: 87 Harrowgate Ave, Pindarra, QLD, 4000
Website: www.quendix.com.au

Visually we'd like the card to be professional and simple.

Attached is our logo.

Our website is www.quendix.com.au

Target Market(s)

Men aged 25-60

Contact Information for Business Card

As listed in project description

Font styles to use
Serif

Requirements
Must have
• Large logo on back of card

```html
<!DOCTYPE html>
<html lang="en">
<head>
<meta charset="utf-8">
<title>Quendix Business Card</title>
<link rel="stylesheet" href="https://fonts.googleapis.com/css2?family=Marcellus&display=swap">
<style>
  :root {
    --backdrop: #35a5d8;
    --navy: #0454a0;
    --sky: #3a9fd6;
    --paper: #ffffff;
    --ink: #0a4f9c;
  }
  html, body {
    margin: 0;
    padding: 0;
    width: 1200px;
    height: 1200px;
    overflow: hidden;
    background: var(--backdrop);
  }
  .card {
    position: absolute;
    left: 347px;
    width: 506px;
    height: 309px;
    background: var(--paper);
    box-shadow: 0 4px 12px rgba(0, 30, 70, 0.45);
  }
  .card--front { top: 273px; }
  .card--back { top: 618px; }
  .card svg {
    display: block;
    width: 100%;
    height: 100%;
  }
  .serif-text {
    font-family: "Marcellus", serif;
  }
  .brand-name { fill: var(--navy); letter-spacing: 3px; }
  .holder-name { fill: var(--paper); font-size: 42px; }
  .holder-role { fill: var(--sky); font-size: 24px; }
  .contact-line { fill: var(--ink); font-size: 28px; letter-spacing: 0.5px; }
  .icon { fill: none; stroke: var(--sky); stroke-width: 2.2; stroke-linecap: round; stroke-linejoin: round; }
  .icon-fill { fill: var(--sky); }
</style>
</head>
<body>

<section class="card card--front" aria-label="Business card front">
  <svg viewBox="0 0 814 498" xmlns="http://www.w3.org/2000/svg">
    <path class="accent-band" fill="var(--sky)" d="M0 0 H276 C205 130 225 390 446 498 H0 Z"/>
    <path class="navy-panel" fill="var(--navy)" d="M0 0 H241 C175 150 215 390 446 498 H0 Z"/>

    <text class="serif-text brand-name" x="560" y="126" font-size="76" text-anchor="middle">QUENDIX</text>

    <g class="icon-phone" transform="translate(317 180)">
      <path class="icon-fill" d="M7 8 C3 12 5 22 12 30 C18 36 22 38 24 35 L21 29 L17 30 C13 27 11 22 11 18 L14 15 L11 8 Z"/>
      <path class="icon" d="M20 8 A9 9 0 0 1 27 15"/>
      <path class="icon" d="M21 2 A15 15 0 0 1 33 14"/>
    </g>
    <g class="icon-mail" transform="translate(316 235)">
      <rect class="icon" x="1" y="2" width="34" height="24"/>
      <path class="icon" d="M1 2 L18 17 L35 2 M1 26 L14 14 M35 26 L22 14"/>
    </g>
    <g class="icon-globe" transform="translate(316 282)">
      <circle class="icon" cx="18" cy="18" r="16"/>
      <ellipse class="icon" cx="18" cy="18" rx="7" ry="16"/>
      <path class="icon" d="M18 2 V34 M2 18 H34 M5 10 H31 M5 26 H31"/>
    </g>

    <text class="serif-text contact-line" x="372" y="211">0471 592 304</text>
    <text class="serif-text contact-line" x="372" y="261">Brent.malvoy@quendix.com.au</text>
    <text class="serif-text contact-line" x="372" y="311">www.quendix.com.au</text>
    <text class="serif-text contact-line" x="372" y="368">87 Harrowgate Ave, Pindarra,</text>
    <text class="serif-text contact-line" x="372" y="400">QLD, 4000</text>

    <text class="serif-text holder-name" x="27" y="406">Brent Malvoy</text>
    <text class="serif-text holder-role" x="27" y="433">General Manager</text>
  </svg>
</section>

<section class="card card--back" aria-label="Business card back">
  <svg viewBox="0 0 814 498" xmlns="http://www.w3.org/2000/svg">
    <text class="serif-text brand-name" x="407" y="290" font-size="118" text-anchor="middle">QUENDIX</text>
  </svg>
</section>

</body>
</html>
```